Bluebrook Irrigation Business Card and Stationary
Business Cards, Envelopes, Stationary, etc.
Simple
Doug Harlan
General Operations Manager
742 Orchard Lane
Irving, TX 75119
doug@irrigatepros.com
www.irrigatepros.com
Li 48391
I want the inside part to list services that we perform.
1. Lawn Sprinkler Repair
2. Lawn Sprinkler Installation
3. Sprinkler System Efficiency Evaluation
4. French/Area Drains
5. Outdoor Lighting
6. Tree/Shrub Planting
7. Landscaping
8. Water Features
9. Sod
10. Backflow Testing
11. Outdoor/Landscape Lighting
12. Soil Test/Analysis
Arrange all of the information as you feel it fits best. I am also getting a PO box today, so the address will e different. I will update that when I have the info. Also, I would like a sticker that we can put on the customers controllers, about business card size that says "call for service," and then has our phone #. I am not opposed to having perfectly rectangular business cards, but am also not sold on it, maybe something with rounded corners.

```html
<!DOCTYPE html>
<html lang="en">
<head>
<meta charset="utf-8">
<title>Bluebrook Irrigation Stationery</title>
<link href="https://fonts.googleapis.com/css2?family=Roboto+Condensed:wght@400;700&display=swap" rel="stylesheet">
<style>
  :root {
    --bg: #e9ecef;
    --paper: #ffffff;
    --blue: #1f7fc4;
    --blue-dark: #15609a;
    --blue-light: #5fb0e6;
    --green: #3f9a2e;
    --ink: #1d3f73;
  }
  * { box-sizing: border-box; margin: 0; padding: 0; }
  html, body { width: 1200px; height: 901px; overflow: hidden; }
  body { background: var(--bg); font-family: "Roboto Condensed", Arial, sans-serif; position: relative; }

  .brand-name { font-weight: 700; color: var(--green); }
  .dot { display: block; border-radius: 50%; background: var(--blue); }

  /* Letterhead */
  .letterhead { position: absolute; left: 40px; top: 40px; width: 430px; height: 620px; background: var(--paper); box-shadow: 0 2px 8px rgba(0,0,0,.15); }
  .letterhead .address { position: absolute; left: 30px; top: 20px; font-size: 11px; line-height: 14px; color: var(--green); font-weight: 700; }
  .letterhead .phones { position: absolute; left: 190px; top: 20px; width: 112px; font-size: 11px; line-height: 14px; color: var(--green); font-weight: 700; display: grid; grid-template-columns: 38px auto; }
  .letterhead .web { position: absolute; left: 100px; top: 74px; font-size: 11px; color: var(--green); font-weight: 700; }
  .letterhead .brand { position: absolute; left: 318px; right: 14px; top: 16px; display: flex; flex-direction: column; align-items: center; gap: 4px; text-align: center; }
  .letterhead .brand .dot { width: 22px; height: 22px; }
  .letterhead .brand-name { font-size: 13px; line-height: 15px; }
  .letterhead .rule-green { position: absolute; left: 30px; top: 100px; bottom: 40px; width: 3px; background: var(--green); }
  .letterhead .rule-blue { position: absolute; left: 38px; top: 100px; bottom: 40px; width: 2px; background: var(--blue); }
  .letterhead .footer { position: absolute; left: 0; right: 0; bottom: 0; height: 24px; background: var(--blue); color: #fff; font-size: 10px; font-weight: 700; letter-spacing: .5px; display: flex; align-items: center; justify-content: center; }

  /* Cards */
  .card { position: absolute; width: 310px; height: 178px; border-radius: 14px; overflow: hidden; box-shadow: 0 2px 8px rgba(0,0,0,.18); }
  .card-front { left: 520px; top: 40px; background: linear-gradient(135deg, var(--blue-light), var(--blue) 55%, var(--blue-dark)); color: #fff; }
  .card-front .brand { position: absolute; left: 0; right: 0; top: 36px; display: flex; align-items: center; justify-content: center; gap: 8px; }
  .card-front .brand .dot { width: 18px; height: 18px; background: #fff; }
  .card-front .brand-name { color: #fff; font-size: 20px; }
  .card-front .contact { position: absolute; left: 0; right: 0; top: 78px; text-align: center; font-size: 10px; line-height: 14px; }
  .card-front .contact .name { font-size: 12px; font-weight: 700; }
  .card-front .tagline { position: absolute; left: 0; right: 0; bottom: 14px; height: 20px; background: var(--blue-dark); font-size: 10px; font-weight: 700; letter-spacing: .4px; display: flex; align-items: center; justify-content: center; }

  .card-back { left: 850px; top: 40px; background: var(--paper); }
  .card-back svg { position: absolute; left: 0; top: 0; }
  .card-back h2 { position: absolute; left: 14px; top: 12px; font-size: 17px; color: var(--green); font-weight: 700; }
  .services { position: absolute; top: 58px; font-size: 10px; line-height: 13px; color: var(--ink); font-weight: 700; list-style: none; }
  .services li { padding-left: 12px; text-indent: -12px; }
  .services.col-a { left: 14px; width: 150px; }
  .services.col-b { left: 172px; width: 128px; }

  /* Envelope */
  .envelope { position: absolute; left: 520px; top: 270px; width: 640px; height: 330px; background: var(--paper); box-shadow: 0 2px 8px rgba(0,0,0,.15); overflow: hidden; }
  .envelope svg.flap { position: absolute; left: 0; top: 0; }
  .envelope .flap-mark { position: absolute; left: 0; right: 0; top: 14px; text-align: center; font-size: 11px; font-weight: 700; color: var(--blue); }
  .envelope .window { position: absolute; left: 34px; top: 150px; width: 220px; height: 64px; border-radius: 10px; background: #e3e5e8; border: 1px solid #c9ccd0; }
  .envelope .brand { position: absolute; right: 34px; top: 206px; display: flex; flex-direction: column; align-items: flex-end; gap: 6px; }
  .envelope .brand-name { font-size: 22px; }
  .envelope .tag-small { font-size: 10px; color: var(--blue); font-weight: 700; }
  .envelope .web-band { position: absolute; left: 0; right: 0; bottom: 0; height: 26px; border-top: 3px solid var(--green); color: var(--green); font-size: 12px; font-weight: 700; letter-spacing: 1px; display: flex; align-items: center; padding-left: 34px; }
</style>
</head>
<body>

<section class="letterhead">
  <div class="address">742 Orchard Lane<br>Irving, TX 75119<br><br>Email:&nbsp;&nbsp;doug@irrigatepros.com</div>
  <div class="phones">
    <span>Phone:</span><span>555-014-2200</span>
    <span>Cell:</span><span>555-014-3311</span>
    <span>Fax:</span><span>555-014-2201</span>
  </div>
  <div class="brand"><span class="dot"></span><span class="brand-name">Bluebrook<br>Irrigation</span></div>
  <div class="web">www.irrigatepros.com</div>
  <div class="rule-green"></div>
  <div class="rule-blue"></div>
  <div class="footer">PROVIDING QUALITY LAWN SPRINKLER SOLUTIONS TO DFW</div>
</section>

<section class="card card-front">
  <div class="brand"><span class="dot"></span><span class="brand-name">Bluebrook Irrigation</span></div>
  <div class="contact">
    <div class="name">Doug Harlan</div>
    <div>General Operations Manager &middot; Li 48391</div>
    <div>555-014-2200 &middot; doug@irrigatepros.com</div>
    <div>www.irrigatepros.com</div>
  </div>
  <div class="tagline">PROVIDING QUALITY LAWN SPRINKLER SOLUTIONS TO DFW</div>
</section>

<section class="card card-back">
  <svg width="310" height="50" viewBox="0 0 310 50">
    <path d="M0 42 Q150 20 310 36" fill="none" stroke="var(--blue)" stroke-width="3"/>
    <path d="M0 47 Q150 28 310 42" fill="none" stroke="var(--green)" stroke-width="2"/>
  </svg>
  <h2>SERVICES WE PROVIDE:</h2>
  <ol class="services col-a">
    <li>1. Lawn Sprinkler Repair</li>
    <li>2. Lawn Sprinkler Installation</li>
    <li>3. Sprinkler System Efficiency Evaluation</li>
    <li>4. French/Area Drains</li>
    <li>5. Outdoor Lighting</li>
    <li>6. Tree/Shrub Planting</li>
  </ol>
  <ol class="services col-b" start="7">
    <li>7. Landscaping</li>
    <li>8. Water Features</li>
    <li>9. Sod</li>
    <li>10. Backflow Testing</li>
    <li>11. Outdoor/Landscape Lighting</li>
    <li>12. Soil Test/Analysis</li>
  </ol>
</section>

<section class="envelope">
  <svg class="flap" width="640" height="90" viewBox="0 0 640 90">
    <path d="M0 0 L320 80 L640 0" fill="#f6f7f8" stroke="#d3d6da" stroke-width="1.5"/>
  </svg>
  <div class="flap-mark">Bluebrook</div>
  <div class="window"></div>
  <div class="brand">
    <span class="brand-name">Bluebrook Irrigation</span>
    <span class="tag-small">PROVIDING QUALITY LAWN SPRINKLER SOLUTIONS TO DFW</span>
  </div>
  <div class="web-band">www.irrigatepros.com</div>
</section>

</body>
</html>
```